Web site for Tree Removal Company

What we are looking for:
-------------------------------
Looking for a wordpress web site, you can provide your own template or we can supply you with one (http://quorvel.plindatheme.net).

What we do
---------------
To see what we do please go to google Australia and google "Tree removal Sydney" or "Tree Removal Melbourne".

Web site requirements
-----------------------------
We prefer you to use our template as it has all our requirements in already.
- Responsive.
- Based on Wordpress.
- Full complaint and compatible with plugs.

Look, Feel and Appearance
------------------------------------
Please use the logo (see attached), for colour scheme, look and feel of the web site.

Thank you for your time and effort!

Target Market(s)

Tree Removal for Residential Homes

Industry/Entity Type

It Company

Number of Pages Required

4 page

Font styles to use
Serif
Sans Serif

Requirements
Must have
• Wordpress
Nice to have
• Original artwork, images and text
Should not have
• non related images or wording

```html
<!DOCTYPE html>
<html lang="en">
<head>
<meta charset="utf-8">
<title>Barkline Tree Services</title>
<link href="https://fonts.googleapis.com/css2?family=Lora:wght@400;700&family=Open+Sans:wght@400;600;700&display=swap" rel="stylesheet">
<style>
:root{
  --green:#2f9a3c;
  --green-dark:#1e3a1d;
  --ink:#2b2b2b;
  --muted:#6b6b6b;
  --line:#e3e3e3;
  --black:#0c0c0c;
  --white:#ffffff;
}
*{margin:0;padding:0;box-sizing:border-box}
html,body{width:1200px;height:3076px;overflow:hidden}
body{position:relative;background:var(--white);font-family:"Open Sans",Arial,sans-serif;color:var(--ink)}
.block{position:absolute;left:0;width:1200px}

/* header + hero */
.hero{top:0;height:440px}
.hero-photo{position:absolute;inset:0;background:linear-gradient(180deg,#8fb3d6 0%,#b9a58c 35%,#8a4a35 55%,#5f8f3a 75%,#7fb04a 100%)}
.topbar{position:absolute;top:0;left:0;width:1200px;height:76px;background:rgba(10,20,10,.82)}
.brand{position:absolute;left:40px;top:14px;display:flex;align-items:center;gap:8px;color:var(--white);font-size:14px;font-weight:700}
.brand-dot{width:34px;height:34px;border-radius:50%;background:var(--green)}
.nav{position:absolute;left:392px;top:0;display:flex;height:50px}
.nav a{display:block;padding:16px 26px;color:var(--white);font-size:15px;text-decoration:none}
.nav a.active{background:var(--green)}
.tollfree{position:absolute;right:96px;top:10px;color:var(--white);font-size:13px;line-height:1.35;display:flex;gap:10px;align-items:center}
.tollfree strong{display:block;font-size:18px}
.hero-caption{position:absolute;left:270px;top:222px;width:660px;height:64px;background:rgba(255,255,255,.35);display:flex;align-items:center;justify-content:center;font-size:27px;font-weight:600;color:var(--ink)}
.hero-arrow{position:absolute;top:234px;width:40px;height:40px}
.hero-wave{position:absolute;left:0;bottom:0}

/* services */
.services{top:520px;height:160px;display:flex;justify-content:center;gap:36px}
.service{width:216px;height:150px;text-align:center;padding-top:18px}
.service.featured{border:1px solid var(--line);box-shadow:0 2px 8px rgba(0,0,0,.08)}
.service svg{width:38px;height:38px}
.service h3{font-family:"Lora",Georgia,serif;font-size:17px;margin:10px 0 8px}
.service.featured h3{color:var(--green)}
.service p{font-size:13px;color:var(--muted);line-height:1.4;padding:0 24px}

/* welcome */
.welcome{top:868px;height:420px}
.welcome-photo{position:absolute;left:100px;top:4px;width:300px;height:400px;background:linear-gradient(160deg,#9cc3e6,#5b7a45 60%,#6d5236);box-shadow:6px 6px 14px rgba(0,0,0,.25)}
.welcome-text{position:absolute;left:460px;top:0;width:640px}
.welcome-text h2{font-family:"Lora",Georgia,serif;font-size:26px;font-weight:400;margin-bottom:26px}
.welcome-text p{font-size:13px;color:var(--muted);line-height:1.7}
.ticks{list-style:none;margin-top:22px}
.ticks li{display:flex;gap:14px;font-size:13px;color:var(--muted);line-height:1.7;margin-bottom:30px}
.ticks svg{flex:0 0 16px;margin-top:4px}
.to-top{position:absolute;width:48px;height:48px;border-radius:50%;border:2px solid var(--ink);display:flex;align-items:center;justify-content:center;background:var(--white)}

/* testimonials */
.testimonials{top:1408px;height:452px;background:linear-gradient(180deg,#6d4a3c,#8b6450 55%,#3d5a2c);text-align:center;color:var(--white)}
.testimonials h2{position:absolute;top:106px;width:100%;font-size:22px;font-weight:600;letter-spacing:3px}
.quote{position:absolute;left:150px;top:172px;width:900px;padding:22px 40px;background:rgba(255,255,255,.28);font-size:14px;line-height:1.6;font-style:italic}
.testimonials .name{position:absolute;top:388px;width:100%;font-size:22px;font-weight:600;letter-spacing:3px}
.dots{position:absolute;top:434px;width:100%;display:flex;justify-content:center;gap:10px}
.dots span{width:8px;height:8px;border-radius:50%;background:var(--white);opacity:.7}

/* tree surgeons */
.surgeons{top:1924px;height:440px;text-align:center}
.surgeons h2{font-family:"Lora",Georgia,serif;font-size:28px;font-weight:400}
.surgeons .sub{font-size:15px;color:var(--muted);margin-top:8px}
.carousel{position:absolute;left:132px;top:116px;width:928px;height:240px;display:flex}
.tile{position:relative;width:232px;height:240px;text-align:left;color:var(--white)}
.tile .label{position:absolute;left:36px;bottom:26px;font-family:"Lora",Georgia,serif;font-size:16px;font-weight:700}
.tile.intro{background:#241c17}
.tile.intro h3{font-family:"Lora",Georgia,serif;font-size:17px;padding:30px 20px 10px}
.tile.intro p{font-size:13px;line-height:1.5;padding:0 20px}
.tile.intro .more{display:block;margin:16px 20px;font-size:12px;font-weight:700}
.t2{background:linear-gradient(180deg,#6f8f3c,#3f5e24)}
.t3{background:linear-gradient(180deg,#8aa65a,#4a6a2c)}
.t4{background:linear-gradient(180deg,#7da0c0,#4d6b33)}
.carousel-nav{position:absolute;top:390px;left:0;width:100%;display:flex;justify-content:center;gap:28px}

/* call to action */
.cta{top:2400px;height:320px;background:linear-gradient(180deg,#23401f,#15250f);color:var(--white);text-align:center}
.cta h2{position:absolute;top:60px;width:100%;font-size:32px;font-weight:600}
.cta-figure{position:absolute;left:112px;top:128px;width:110px;height:190px;background:linear-gradient(180deg,#6a4a36,#2c3b55)}
.contact{position:absolute;top:150px;width:280px;text-align:center}
.contact .lbl{font-size:18px;margin-top:10px}
.contact .val{font-size:30px;margin-top:2px}

/* partners */
.partners{top:2760px;height:220px;display:flex;justify-content:space-around;align-items:center;padding:0 110px}
.badge{background:#d9d9d9}
.badge.round{width:64px;height:64px;border-radius:50%;background:#2a6b2f}
.badge.bar{width:170px;height:28px;background:#c9b23a}
.badge.wide{width:190px;height:44px;background:#8a9aa8}
.badge.square{width:60px;height:60px;background:#3e7fb8}

/* footer */
.footer{top:2960px;height:116px}
.socials{position:absolute;top:52px;left:0;width:100%;display:flex;justify-content:center;gap:36px}
.socials span{width:18px;height:18px;border-radius:50%;background:var(--white)}
.copyright{position:absolute;top:92px;width:100%;text-align:center;font-size:11px;color:#888}
</style>
</head>
<body>

<header class="block hero">
  <div class="hero-photo" role="img" aria-label="Photo of a brick family home with a trimmed front garden and hedges"></div>
  <div class="topbar">
    <div class="brand"><span class="brand-dot"></span>Barkline</div>
    <nav class="nav">
      <a class="active" href="#">Home</a>
      <a href="#">About Us</a>
      <a href="#">Services</a>
      <a href="#">Contact Us</a>
    </nav>
    <div class="tollfree">
      <svg width="20" height="20" viewBox="0 0 24 24" fill="#fff"><path d="M6.6 10.8a15 15 0 0 0 6.6 6.6l2.2-2.2c.3-.3.7-.4 1-.2 1.1.4 2.3.6 3.6.6.6 0 1 .4 1 1V20c0 .6-.4 1-1 1A17 17 0 0 1 3 4c0-.6.4-1 1-1h3.5c.6 0 1 .4 1 1 0 1.3.2 2.5.6 3.6.1.3 0 .7-.2 1z"/></svg>
      <div>Toll Free :<strong>0800 4271956</strong></div>
    </div>
  </div>
  <svg class="hero-arrow" style="left:278px" viewBox="0 0 40 40"><path d="M24 10 14 20l10 10" stroke="#fff" stroke-width="3" fill="none"/></svg>
  <div class="hero-caption">Let us beautify your outdoor living space!</div>
  <svg class="hero-arrow" style="left:882px" viewBox="0 0 40 40"><path d="M16 10l10 10-10 10" stroke="#fff" stroke-width="3" fill="none"/></svg>
  <svg class="hero-wave" width="1200" height="60" viewBox="0 0 1200 60"><path d="M0 30 Q600 -10 1200 30 L1200 60 L0 60Z" fill="#fff"/><path d="M0 30 Q600 -10 1200 30" stroke="#1e3a1d" stroke-width="4" fill="none"/></svg>
</header>

<section class="block services">
  <div class="service">
    <svg viewBox="0 0 38 38" fill="none" stroke="#333" stroke-width="2"><circle cx="19" cy="14" r="10"/><path d="M19 24v12M12 36h14"/></svg>
    <h3>Tree Removal</h3>
    <p>Lorem ipsum dolor sit amet, quisi adipiscing elit. Praesent vestibulum</p>
  </div>
  <div class="service">
    <svg viewBox="0 0 38 38" fill="#333"><rect x="8" y="18" width="22" height="14" rx="2"/><rect x="4" y="30" width="30" height="4"/></svg>
    <h3>Stump Grinding</h3>
    <p>Lorem ipsum dolor sit amet, quisi adipiscing elit. Praesent vestibulum</p>
  </div>
  <div class="service">
    <svg viewBox="0 0 38 38" fill="none" stroke="#333" stroke-width="2"><path d="M19 4v30M19 12l-8-6M19 12l8-6M19 20l-10-6M19 20l10-6"/></svg>
    <h3>Tree Pruning</h3>
    <p>Lorem ipsum dolor sit amet, quisi adipiscing elit. Praesent vestibulum</p>
  </div>
  <div class="service featured">
    <svg viewBox="0 0 38 38" fill="#2f9a3c"><path d="M19 4 9 20h6l-6 10h20l-6-10h6z"/><rect x="17" y="30" width="4" height="6"/></svg>
    <h3>Arborist</h3>
    <p>Lorem ipsum dolor sit amet, quisi adipiscing elit. Praesent vestibulum</p>
  </div>
</section>

<section class="block welcome">
  <div class="welcome-photo" role="img" aria-label="Photo of an arborist in safety gear climbing a tree trunk"></div>
  <div class="welcome-text">
    <h2>Welcome to our website</h2>
    <p>Aenean accumsan et odio sollicitudin dignissim quis blandit praesent luptatum zzril delenit augue duis dolore te feugait nulla facilisi. Typi non habent claritatem insitam est usus legentis in iis qui.</p>
    <ul class="ticks">
      <li><svg width="16" height="16" viewBox="0 0 16 16"><path d="M2 8l4 4 8-9" stroke="#2f9a3c" stroke-width="2.5" fill="none"/></svg><span>Accumsan et odio sollicitudin dignissim qui blandit praesent luptatum zzril delenit augue duis dolore te feugait nulla facilisi. Typi non habent claritatem insitam est usus legentis in iis quorum esse.</span></li>
      <li><svg width="16" height="16" viewBox="0 0 16 16"><path d="M2 8l4 4 8-9" stroke="#2f9a3c" stroke-width="2.5" fill="none"/></svg><span>Accumsan et odio sollicitudin dignissim qui blandit praesent luptatum zzril delenit augue duis dolore te feugait nulla facilisi. Typi non habent claritatem insitam est usus legentis in iis quorum esse.</span></li>
      <li><svg width="16" height="16" viewBox="0 0 16 16"><path d="M2 8l4 4 8-9" stroke="#2f9a3c" stroke-width="2.5" fill="none"/></svg><span>Accumsan et odio sollicitudin dignissim qui blandit praesent luptatum zzril delenit augue duis dolore te feugait nulla facilisi. Typi non habent claritatem insitam est usus legentis in iis quorum esse.</span></li>
    </ul>
  </div>
  <div class="to-top" style="left:1088px;top:414px"><svg width="18" height="12" viewBox="0 0 18 12"><path d="M2 10l7-7 7 7" stroke="#2b2b2b" stroke-width="2.5" fill="none"/></svg></div>
</section>

<section class="block testimonials" role="img" aria-label="Photo backdrop of a brick wall behind garden shrubs">
  <h2>Testimonials</h2>
  <p class="quote">"Accumsan et odio sollicitudin dignissim qui blandit praesent luptatum zzril delenit augue duis dolore te feugait nulla facilisi. Typi non habent claritatem insitam est usus legentis."</p>
  <p class="name">Nora Whitfield</p>
  <div class="dots"><span></span><span></span><span></span></div>
</section>

<section class="block surgeons">
  <h2>Tree surgeons</h2>
  <p class="sub">Expert tree surgeons for homes and businesses</p>
  <div class="carousel">
    <div class="tile intro">
      <h3>Tree Planting</h3>
      <p>Lorem ipsum dolor sit amet, quisi adipiscing elit praesent luptatum zzril delenit augue.</p>
      <span class="more">» Read more</span>
    </div>
    <div class="tile t2" role="img" aria-label="Photo of a worker trimming a hedge"><span class="label">Hedge Trimming</span></div>
    <div class="tile t3" role="img" aria-label="Photo of a tree surgeon working among branches"><span class="label">Tree Surgery</span></div>
    <div class="tile t4" role="img" aria-label="Photo of an arborist roped into a tall tree"></div>
  </div>
  <div class="carousel-nav">
    <svg width="14" height="18" viewBox="0 0 14 18"><path d="M11 2 4 9l7 7" stroke="#222" stroke-width="3" fill="none"/></svg>
    <svg width="14" height="18" viewBox="0 0 14 18"><path d="M3 2l7 7-7 7" stroke="#222" stroke-width="3" fill="none"/></svg>
  </div>
</section>

<section class="block cta">
  <h2>Get FREE quotes from tree removal experts</h2>
  <div class="cta-figure" role="img" aria-label="Illustration of a lumberjack holding an axe"></div>
  <div class="contact" style="left:460px">
    <svg width="26" height="26" viewBox="0 0 24 24" fill="#fff"><path d="M6.6 10.8a15 15 0 0 0 6.6 6.6l2.2-2.2c.3-.3.7-.4 1-.2 1.1.4 2.3.6 3.6.6.6 0 1 .4 1 1V20c0 .6-.4 1-1 1A17 17 0 0 1 3 4c0-.6.4-1 1-1h3.5c.6 0 1 .4 1 1 0 1.3.2 2.5.6 3.6.1.3 0 .7-.2 1z"/></svg>
    <p class="lbl">Call Us</p>
    <p class="val">0800 4271956</p>
  </div>
  <div class="contact" style="left:760px;width:300px">
    <svg width="26" height="26" viewBox="0 0 24 24" fill="#fff"><path d="M2 11 22 3l-7 19-4-8z"/></svg>
    <p class="lbl">Mail Us</p>
    <p class="val">hello@barkline.example</p>
  </div>
</section>

<section class="block partners">
  <span class="badge round"></span>
  <span class="badge bar"></span>
  <span class="badge wide"></span>
  <span class="badge square"></span>
</section>

<footer class="block footer">
  <svg style="position:absolute;top:0;left:0" width="1200" height="116" viewBox="0 0 1200 116"><path d="M0 36 Q600 -4 1200 36 L1200 116 L0 116Z" fill="#0c0c0c"/></svg>
  <div class="socials"><span></span><span></span><span></span></div>
  <p class="copyright">Copyright © 2016 | Privacy Policy</p>
  <div class="to-top" style="left:1092px;top:54px;width:40px;height:40px;border-color:#fff"><svg width="16" height="10" viewBox="0 0 18 12"><path d="M2 10l7-7 7 7" stroke="#0c0c0c" stroke-width="3" fill="none"/></svg></div>
</footer>

</body>
</html>
```